CEO Business card - hotels and restaurant

Business card for the General Manager of 3 different businesses: 2 hotels and 1 restaurant:
Quinta Serrana Hotel
Casa Ormonde - Miravel Hotel
pão com toda alegria restaurant
Name and contact details:
Rui Fontelas Marques
CEO
E-mail: rui.marques@quintaserranahotel.com
Mobile: +351 917 443 261
Please find the attached logos. You may also google it for the 3 businesses

Industry/Entity Type

Hospitality

Contact Information for Business Card

Rui Fontelas Marques
CEO

Font styles to use
Script

Colors

Designer to choose colors to be used in the design.

Requirements
Must have
• Front - Name, position and contact details
• Back - Businesses logos and info of each one
• HOTEL QUINTA SERRANA
• Address: Rua Padre Anselmo - Nº 173 | 2440-627 BATALHA - PORTUGAL
• Phone: +351 244 581 392
• E-mail: geral@quintaserranahotel.pt
• HOTEL CASA ORMONDE - MIRAVEL
• Address: Avenida dos Cedros, s/n | 7350-218 ELVAS - PORTUGAL
• Phone: +351 268 472 519
• E-mail: geral@hotelcormonde-miravel.pt
• "pão com toda alegria" RESTAURANT
• Address: Estrada do Pinhal, 42 | 2440-356 BATALHA - PORTUGAL
• Phone: +351 244 615 284
• E-mail: info@pcta.pt
Nice to have
• Something elegant and stylish but professional and very wow effect

```html
<!DOCTYPE html>
<html lang="pt">
<head>
<meta charset="utf-8">
<title>Rui Fontelas Marques – Business Cards</title>
<link href="https://fonts.googleapis.com/css2?family=Berkshire+Swash&family=Jost:wght@300;400;500&display=swap" rel="stylesheet">
<style>
  :root {
    --bg: #dcd7d0;
    --gold: #efc36c;
    --gold-dark: #b8873a;
    --red: #e02a30;
    --magenta: #e8126e;
    --black: #050505;
    --ink: #1b1b1b;
    --white: #ffffff;
    --resto: #8a1a3c;
    --ormonde: #1a8fd0;
    --quinta: #e0197a;
  }
  * { margin: 0; padding: 0; box-sizing: border-box; }
  html, body { width: 1200px; height: 1200px; overflow: hidden; }
  body { background: var(--bg); position: relative; font-family: "Jost", sans-serif; }

  .card {
    position: absolute;
    width: 514px;
    height: 308px;
    box-shadow: 0 4px 14px rgba(0,0,0,.25);
    overflow: hidden;
  }
  .card--front-red { left: 64px; top: 262px; background: linear-gradient(90deg, var(--red), var(--magenta)); }
  .card--front-black { left: 64px; top: 630px; background: var(--black); }
  .card--back { background: var(--white); color: var(--ink); }
  .card--back.top { left: 622px; top: 262px; }
  .card--back.bottom { left: 622px; top: 630px; }

  .title-art { position: absolute; left: 0; top: 0; }
  .title-art text { font-family: "Berkshire Swash", cursive; fill: var(--gold); font-size: 25px; }

  .monogram-band { position: absolute; left: 0; top: 31px; width: 514px; height: 142px; }
  .monogram-fill {
    position: absolute; left: 0; top: 40px; width: 514px; height: 126px;
    background: linear-gradient(90deg, rgba(239,195,108,.28), rgba(184,135,58,.42), rgba(239,195,108,.28));
  }

  .holder { position: absolute; left: 21px; top: 196px; color: var(--white); }
  .holder-name { font-weight: 500; font-size: 17.5px; letter-spacing: .2px; line-height: 22px; }
  .holder-role { font-weight: 400; font-size: 11px; letter-spacing: 5px; line-height: 14px; }
  .holder-line { display: flex; align-items: center; gap: 6px; font-weight: 300; font-size: 15px; margin-top: 7px; line-height: 16px; }
  .holder-line:first-of-type { margin-top: 12px; }
  .holder-line svg { width: 19px; height: 19px; flex: none; }

  .venue { position: absolute; left: 32px; width: 460px; }
  .venue:nth-child(1) { top: 40px; }
  .venue:nth-child(2) { top: 122px; }
  .venue:nth-child(3) { top: 203px; }
  .venue-mark { position: absolute; left: 0; top: 10px; width: 42px; height: 42px; }
  .venue-mark.circle { border-radius: 50%; }
  .venue--resto .venue-mark { background: var(--resto); }
  .venue--ormonde .venue-mark { background: var(--ormonde); }
  .venue--quinta .venue-mark { background: var(--quinta); }
  .venue-body { position: absolute; left: 54px; top: 0; width: 406px; }
  .venue-head { display: flex; justify-content: space-between; align-items: baseline; }
  .venue-name { font-weight: 400; font-size: 16.5px; line-height: 22px; }
  .venue-type { font-weight: 400; font-size: 10px; letter-spacing: 4.5px; }
  .venue-line { display: flex; align-items: center; gap: 4px; font-weight: 300; font-size: 13px; line-height: 22px; white-space: nowrap; }
  .venue-line svg { width: 18px; height: 18px; flex: none; }
  .venue-line .gap { width: 6px; }
  .venue--resto svg { color: var(--resto); }
  .venue--ormonde svg { color: var(--ormonde); }
  .venue--quinta svg { color: var(--quinta); }
</style>
</head>
<body>

<svg width="0" height="0" style="position:absolute" aria-hidden="true">
  <defs>
    <symbol id="icon-pin" viewBox="0 0 20 20">
      <circle cx="10" cy="10" r="10" fill="currentColor"/>
      <path d="M10 4.2a3.8 3.8 0 0 0-3.8 3.8c0 2.8 3.8 7.6 3.8 7.6s3.8-4.8 3.8-7.6A3.8 3.8 0 0 0 10 4.2z" fill="#fff"/>
      <circle cx="10" cy="8" r="1.5" fill="currentColor"/>
    </symbol>
    <symbol id="icon-phone" viewBox="0 0 20 20">
      <circle cx="10" cy="10" r="10" fill="currentColor"/>
      <path d="M7 4.5c.6-.3 1.2 0 1.4.6l.7 2c.2.5 0 1-.4 1.3l-.6.4c.4 1.4 1.3 2.7 2.5 3.6l.6-.4c.4-.3 1-.3 1.3.1l1.5 1.5c.4.5.3 1.1-.2 1.5-1.3 1-3.1.9-4.5-.3C6.9 12.7 5.6 10.3 5.5 7.6c0-1.3.5-2.5 1.5-3.1z" fill="#fff"/>
    </symbol>
    <symbol id="icon-mail" viewBox="0 0 20 20">
      <circle cx="10" cy="10" r="10" fill="currentColor"/>
      <rect x="4.6" y="6.2" width="10.8" height="7.6" rx="1" fill="none" stroke="#fff" stroke-width="1.4"/>
      <path d="M5 7l5 3.8L15 7" fill="none" stroke="#fff" stroke-width="1.4"/>
    </symbol>
  </defs>
</svg>

<!-- Front, red -->
<section class="card card--front-red">
  <svg class="title-art" width="514" height="308" viewBox="0 0 514 308">
    <g fill="var(--gold)">
      <path d="M0 68 C30 66 60 66 100 70 C60 72 30 73 0 73 Z"/>
      <path d="M414 70 C450 66 480 66 514 67 L514 72 C480 72 450 72 414 70 Z"/>
      <path d="M0 106 C40 108 70 110 98 110 C70 114 40 115 0 114 Z"/>
      <path d="M418 110 C450 108 480 106 514 105 L514 113 C480 114 450 113 418 110 Z"/>
      <path d="M0 144 C60 146 110 148 142 148 C110 153 60 154 0 152 Z"/>
      <path d="M372 148 C420 145 470 143 514 143 L514 151 C470 152 420 152 372 148 Z"/>
    </g>
    <text x="257" y="78" text-anchor="middle">pão com toda alegria</text>
    <text x="257" y="118" text-anchor="middle">Casa Ormonde - Miravel</text>
    <text x="257" y="157" text-anchor="middle">Quinta Serrana</text>
  </svg>
  <div class="holder">
    <p class="holder-name">Rui Fontelas Marques</p>
    <p class="holder-role">CEO</p>
    <p class="holder-line"><svg style="color:var(--gold)"><use href="#icon-mail"/></svg>rui.marques@quintaserranahotel.com</p>
    <p class="holder-line"><svg style="color:var(--gold)"><use href="#icon-phone"/></svg>+351 917 443 261</p>
  </div>
</section>

<!-- Front, black -->
<section class="card card--front-black">
  <svg class="monogram-band" width="514" height="142" viewBox="0 0 514 142" aria-hidden="true">
    <path d="M0 2 Q257 -4 514 2" fill="none" stroke="var(--gold)" stroke-width="3"/>
    <path d="M0 138 Q257 132 514 138" fill="none" stroke="var(--gold)" stroke-width="3"/>
  </svg>
  <div class="monogram-fill" role="img" aria-label="Gold calligraphic monogram flourish of the three venues' initials"></div>
  <div class="holder">
    <p class="holder-name">Rui Fontelas Marques</p>
    <p class="holder-role">CEO</p>
    <p class="holder-line"><svg style="color:var(--gold)"><use href="#icon-mail"/></svg>rui.marques@quintaserranahotel.com</p>
    <p class="holder-line"><svg style="color:var(--gold)"><use href="#icon-phone"/></svg>+351 917 443 261</p>
  </div>
</section>

<!-- Backs -->
<section class="card card--back top">
  <div class="venue venue--resto">
    <span class="venue-mark"></span>
    <div class="venue-body">
      <div class="venue-head"><h2 class="venue-name">pão com toda alegria</h2><span class="venue-type">RESTAURANT</span></div>
      <p class="venue-line"><svg><use href="#icon-pin"/></svg>Estrada do Pinhal, 42 | 2440-356 BATALHA - PORTUGAL</p>
      <p class="venue-line"><svg><use href="#icon-phone"/></svg>+351 244 615 284<span class="gap"></span><svg><use href="#icon-mail"/></svg>info@pcta.pt</p>
    </div>
  </div>
  <div class="venue venue--ormonde">
    <span class="venue-mark"></span>
    <div class="venue-body">
      <div class="venue-head"><h2 class="venue-name">Casa Ormonde - Miravel</h2><span class="venue-type">HOTEL</span></div>
      <p class="venue-line"><svg><use href="#icon-pin"/></svg>Avenida dos Cedros, s/n | 7350-218 ELVAS - PORTUGAL</p>
      <p class="venue-line"><svg><use href="#icon-phone"/></svg>+351 268 472 519<span class="gap"></span><svg><use href="#icon-mail"/></svg>geral@hotelcormonde-miravel.pt</p>
    </div>
  </div>
  <div class="venue venue--quinta">
    <span class="venue-mark circle"></span>
    <div class="venue-body">
      <div class="venue-head"><h2 class="venue-name">Quinta Serrana</h2><span class="venue-type">HOTEL</span></div>
      <p class="venue-line"><svg><use href="#icon-pin"/></svg>Rua Padre Anselmo - Nº 173 | 2440-627 BATALHA - PORTUGAL</p>
      <p class="venue-line"><svg><use href="#icon-phone"/></svg>+351 244 581 392<span class="gap"></span><svg><use href="#icon-mail"/></svg>geral@quintaserranahotel.pt</p>
    </div>
  </div>
</section>

<section class="card card--back bottom">
  <div class="venue venue--resto">
    <span class="venue-mark"></span>
    <div class="venue-body">
      <div class="venue-head"><h2 class="venue-name">pão com toda alegria</h2><span class="venue-type">RESTAURANT</span></div>
      <p class="venue-line"><svg><use href="#icon-pin"/></svg>Estrada do Pinhal, 42 | 2440-356 BATALHA - PORTUGAL</p>
      <p class="venue-line"><svg><use href="#icon-phone"/></svg>+351 244 615 284<span class="gap"></span><svg><use href="#icon-mail"/></svg>info@pcta.pt</p>
    </div>
  </div>
  <div class="venue venue--ormonde">
    <span class="venue-mark"></span>
    <div class="venue-body">
      <div class="venue-head"><h2 class="venue-name">Casa Ormonde - Miravel</h2><span class="venue-type">HOTEL</span></div>
      <p class="venue-line"><svg><use href="#icon-pin"/></svg>Avenida dos Cedros, s/n | 7350-218 ELVAS - PORTUGAL</p>
      <p class="venue-line"><svg><use href="#icon-phone"/></svg>+351 268 472 519<span class="gap"></span><svg><use href="#icon-mail"/></svg>geral@hotelcormonde-miravel.pt</p>
    </div>
  </div>
  <div class="venue venue--quinta">
    <span class="venue-mark circle"></span>
    <div class="venue-body">
      <div class="venue-head"><h2 class="venue-name">Quinta Serrana</h2><span class="venue-type">HOTEL</span></div>
      <p class="venue-line"><svg><use href="#icon-pin"/></svg>Rua Padre Anselmo - Nº 173 | 2440-627 BATALHA - PORTUGAL</p>
      <p class="venue-line"><svg><use href="#icon-phone"/></svg>+351 244 581 392<span class="gap"></span><svg><use href="#icon-mail"/></svg>geral@quintaserranahotel.pt</p>
    </div>
  </div>
</section>

</body>
</html>
```